Furniture retail store requires in store display board design.

I am launching a new bed buying concept in my retail stores and require a point of sale graphic to explain the purchase process to consumers.
1.Select base style.(Including headboard) + 2. Customise legs and storage options. + 3.Choose Colours. + 4. Add your perfect mattress. = Your perfect nights sleep.
I'm imagining a sketchy/whiteboard/chalkboard type effect. The main boards will hang above a bed and will be 150cm wide x 35cm high.
Consumers 30yo+
Retail

```html
<!DOCTYPE html>
<html lang="en">
<head>
<meta charset="utf-8">
<title>4 Easy Steps to a Perfect Sleep</title>
<link href="https://fonts.googleapis.com/css2?family=Cabin+Sketch:wght@400;700&family=Arimo:ital,wght@0,400;0,700;1,400&display=swap" rel="stylesheet">
<style>
  :root {
    --blue-deep: #0d47c9;
    --blue-mid: #1f6ff0;
    --blue-light: #4e95fb;
    --white: #ffffff;
    --red: #e8222a;
    --ink: #111111;
    --cream-1: #fbf1d6;
    --cream-2: #efdcae;
    --cream-3: #fffaf0;
    --photo-grey-1: #e9e6e2;
    --photo-grey-2: #b9b2aa;
    --photo-bed-1: #e7ded3;
    --photo-bed-2: #a7978a;
    --photo-white: #f4f4f4;
  }
  * { box-sizing: border-box; margin: 0; padding: 0; }
  html, body { width: 1200px; height: 280px; overflow: hidden; background: var(--white); }
  .board {
    position: relative; width: 1200px; height: 280px; overflow: hidden;
    background: radial-gradient(ellipse at 45% 55%, var(--blue-light) 0%, var(--blue-mid) 45%, var(--blue-deep) 100%);
    font-family: "Cabin Sketch", cursive;
    color: var(--white);
  }
  .headline {
    position: absolute; left: 145px; top: 12px;
    font-size: 43px; font-weight: 700; letter-spacing: 2px; text-transform: uppercase;
    white-space: nowrap; line-height: 1.1;
  }
  .headline-number { position: absolute; left: 72px; top: 0; width: 66px; height: 66px; }
  .step-label {
    position: absolute; font-size: 13.5px; font-weight: 700; text-transform: uppercase;
    letter-spacing: 0.5px; white-space: nowrap; line-height: 1.2;
  }
  .step-label-base { left: 33px; top: 68px; font-size: 17px; }
  .step-label-storage { left: 228px; top: 241px; }
  .step-label-colours { left: 495px; top: 85px; font-size: 15px; }
  .step-label-mattress { left: 668px; top: 241px; }
  .step-note {
    position: absolute; left: 38px; top: 90px;
    font-family: "Arimo", sans-serif; font-style: italic; font-size: 13px; line-height: 1.2;
  }
  .photo { position: absolute; }
  .photo-base { left: 22px; top: 110px; width: 156px; height: 152px; background: linear-gradient(180deg, var(--photo-white), var(--photo-grey-1)); }
  .photo-storage { left: 258px; top: 85px; width: 199px; height: 137px; background: linear-gradient(160deg, var(--photo-grey-1), var(--photo-grey-2)); }
  .photo-mattress { left: 668px; top: 85px; width: 175px; height: 143px; background: linear-gradient(170deg, var(--photo-bed-1), var(--photo-bed-2)); }
  .step-number {
    position: absolute; font-family: "Arimo", sans-serif; font-weight: 700;
    color: var(--red); font-size: 22px; line-height: 1;
  }
  .step-number-1 { left: 38px; top: 117px; }
  .step-number-2 { left: 266px; top: 202px; }
  .step-number-3 { left: 546px; top: 168px; font-size: 26px; }
  .step-number-4 { left: 708px; top: 140px; font-size: 24px; }
  .swatches {
    position: absolute; left: 487px; top: 110px; width: 176px; height: 97px;
    border-collapse: collapse; background: var(--white); table-layout: fixed;
  }
  .swatches td {
    border: 1px solid var(--ink); height: 12px; padding: 0 2px;
    font-size: 7.5px; font-weight: 700; color: var(--ink); text-transform: uppercase;
    line-height: 1; white-space: nowrap; overflow: visible;
  }
  .swatches .name { width: 52px; }
  .swatches .swatch { width: 36px; }
  .connector { position: absolute; left: 0; top: 0; width: 1200px; height: 280px; pointer-events: none; }
  .finale {
    position: absolute; left: 906px; top: 0; width: 294px; height: 280px;
    background: linear-gradient(180deg, var(--cream-3) 0%, var(--cream-1) 45%, var(--cream-2) 100%);
    font-family: "Arimo", sans-serif; font-weight: 700; color: var(--ink); text-align: center;
  }
  .finale-title { position: absolute; left: 0; right: 0; top: 12px; font-size: 33px; line-height: 1.12; }
  .finale-tagline { position: absolute; left: 0; right: 0; top: 198px; font-size: 31px; line-height: 1.12; }
</style>
</head>
<body>
<main class="board">
  <svg class="headline-number" viewBox="0 0 62 62" aria-hidden="true">
    <polygon fill="var(--white)" points="31,1 37,14 51,7 47,22 61,25 49,34 58,46 43,45 43,60 31,51 19,60 19,45 4,46 13,34 1,25 15,22 11,7 25,14"/>
    <text x="31" y="47" text-anchor="middle" font-family="Arimo, sans-serif" font-weight="700" font-size="44" fill="var(--red)">4</text>
  </svg>
  <h1 class="headline">Easy steps to a perfect sleep!</h1>

  <p class="step-label step-label-base">Select base style.</p>
  <p class="step-note">(Including headboard)</p>
  <div class="photo photo-base" role="img" aria-label="White upholstered bed base with tall buttoned headboard"></div>
  <span class="step-number step-number-1">1</span>

  <div class="photo photo-storage" role="img" aria-label="Dark bed base with lift-up storage compartment open"></div>
  <span class="step-number step-number-2">2</span>
  <p class="step-label step-label-storage">Customise legs and storage options</p>

  <p class="step-label step-label-colours">Choose colours.</p>
  <table class="swatches">
    <tr><td class="name">Cream</td><td class="swatch" style="background:#f6efd6"></td><td class="name">Sky</td><td class="swatch" style="background:#6a7fe0"></td></tr>
    <tr><td class="name">Pink</td><td class="swatch" style="background:#f2c4cc"></td><td class="name">Steel</td><td class="swatch" style="background:#4a4aa8"></td></tr>
    <tr><td class="name">Burgundy</td><td class="swatch" style="background:#a0263a"></td><td class="name">Navy</td><td class="swatch" style="background:#2a2360"></td></tr>
    <tr><td class="name">Lilac</td><td class="swatch" style="background:#c9a6e6"></td><td class="name">Black</td><td class="swatch" style="background:#161616"></td></tr>
    <tr><td class="name">Purple</td><td class="swatch" style="background:#7b2fb6"></td><td class="name">Hot pink</td><td class="swatch" style="background:#e8288a"></td></tr>
    <tr><td class="name">Bone</td><td class="swatch" style="background:#e6dcb8"></td><td class="name">Slate</td><td class="swatch" style="background:#5a4a66"></td></tr>
    <tr><td class="name">Forest</td><td class="swatch" style="background:#2f8a4a"></td><td class="name">Chocolate</td><td class="swatch" style="background:#4a2e22"></td></tr>
    <tr><td class="name">Teal</td><td class="swatch" style="background:#1a9a7a"></td><td class="name">Gold</td><td class="swatch" style="background:#ece07a"></td></tr>
  </table>
  <span class="step-number step-number-3">3</span>

  <div class="photo photo-mattress" role="img" aria-label="Bed with thick pillow-top mattress in a bedroom"></div>
  <span class="step-number step-number-4">4</span>
  <p class="step-label step-label-mattress">Add your perfect mattress</p>

  <svg class="connector" viewBox="0 0 1200 280" aria-hidden="true">
    <g fill="none" stroke="var(--white)" stroke-width="9" stroke-linecap="round">
      <path d="M178 168 C200 120 235 112 258 128"/>
      <path d="M446 198 C470 232 520 228 546 200"/>
      <path d="M624 118 C650 78 700 82 716 118"/>
    </g>
    <g fill="none" stroke="var(--red)" stroke-width="5" stroke-linecap="round">
      <path d="M178 168 C200 120 235 112 258 128"/>
      <path d="M446 198 C470 232 520 228 546 200"/>
      <path d="M624 118 C650 78 700 82 716 118"/>
    </g>
    <g fill="var(--red)">
      <polygon points="268,138 248,134 259,120"/>
      <polygon points="552,190 548,210 535,199"/>
      <polygon points="720,130 708,116 724,110"/>
      <polygon points="862,110 882,110 882,88 906,136 882,184 882,162 862,162"/>
    </g>
  </svg>

  <aside class="finale" role="img" aria-label="Woman sleeping peacefully in soft white bedding in warm morning light">
    <p class="finale-title">Your perfect<br>nights sleep!</p>
    <p class="finale-tagline">The choice<br>is yours!</p>
  </aside>
</main>
</body>
</html>
```